Tag Rugby (Sport) Website

We are looking to redesign the home page of Celtic Flagball Federation (www.flagballhub.ie). We are an adult sports company, with 10,000 players around Ireland, aged 22 to 35, equally divided between male and female. Tag is a fantastic way to keep fit but to meet new people - so the website should be very clear, bright and fun to reflect the social nature of the sport.

Target Market(s)

22-35 ABC1 equally male and female.

Industry/Entity Type

Adult

Font styles to use
Sans Serif

Requirements
Must have
• It MUST have all the elements on this "home made" page. http://www.flagballhub.ie/defaultnew.aspx

The structure of the website has been signed off...we just require the thing to be designed and brought together

We need the 3 ad spaces to be designed:
1. Square ad on left should have following text:
Spring back into Action! Play Tag from Mar to May. Last Few Spaces Available - REGISTER NOW! (Use the Flagballhub.ie ball logo)

2. Top right ad to be designed with following text:
Find your Nearest Tag Venue (include icon with outline Map of Ireland)

3. Bottom right ad to be designed with following text:
Tag Events Calendar (with some calendar icon)

The dropdown menu items should be displayed vertically (not horizontally) - similar to drop downs on www.goflagsport.com
Nice to have
• We also require Social Media icons to be prominent (in own separate section?) on header and footer

```html
<!DOCTYPE html>
<html lang="en">
<head>
<meta charset="utf-8">
<title>Celtic Flagball Federation – Home</title>
<link href="https://fonts.googleapis.com/css2?family=Roboto:wght@300;400;500;700&display=swap" rel="stylesheet">
<style>
:root{
  --ink:#000;
  --slate:#3d4b5e;
  --white:#fff;
  --muted:#6b6b6b;
  --red:#d71920;
  --orange:#f5a21b;
  --grass:#2f8a3c;
  --line:#9aa5b3;
}
*{box-sizing:border-box;margin:0;padding:0}
html,body{width:1200px;height:1000px;overflow:hidden;background:var(--ink)}
body{font-family:"Roboto",Arial,sans-serif;position:relative}
a{text-decoration:none;color:inherit}
.abs{position:absolute}

.hero-photo{left:0;top:0;width:1200px;height:555px;
  background:
    radial-gradient(ellipse 260px 200px at 930px 240px,rgba(214,170,140,.35),transparent 70%),
    radial-gradient(ellipse 240px 180px at 120px 200px,rgba(214,170,140,.3),transparent 70%),
    radial-gradient(ellipse 380px 140px at 600px 300px,rgba(205,160,130,.22),transparent 70%),
    linear-gradient(180deg,rgba(0,0,0,0) 0%,rgba(0,0,0,0) 82%,rgba(20,22,30,.75) 100%),
    linear-gradient(90deg,rgba(0,0,0,.18) 0%,rgba(0,0,0,0) 30%,rgba(0,0,0,0) 70%,rgba(0,0,0,.18) 100%),
    linear-gradient(180deg,#dfe3e6 0%,#c9d0cf 12%,#7c8a72 22%,#4d6a45 30%,#3a8f4a 44%,#2a9a48 58%,#1f8a3c 74%,#1b6d32 88%,#1e2a24 100%)}

.brand{left:226px;top:0;width:140px;height:114px;background:var(--white);
  display:flex;flex-direction:column;align-items:center;justify-content:center;gap:6px;color:var(--red);font-weight:700}
.brand__name{font-size:26px;letter-spacing:1px}
.brand__url{font-size:11px}

.social{left:400px;top:27px;display:flex;gap:9px}
.social span{width:20px;height:20px;border-radius:50%;background:#5c5c5c;display:block}
.utility{left:507px;top:31px;font-size:10px;color:var(--muted);white-space:nowrap}
.login{left:992px;top:0;width:87px;height:26px;background:var(--white);border-radius:0 0 5px 5px;
  font-size:10px;color:#888;display:flex;align-items:center;justify-content:center;gap:8px}
.login i{border:5px solid transparent;border-top:6px solid #999;margin-top:5px}

.main-nav{left:366px;top:62px;width:713px;height:52px;background:var(--ink);display:flex;align-items:center;list-style:none}
.main-nav li{font-size:12px;color:var(--white);flex:none;text-align:center;position:relative;white-space:nowrap}
.main-nav li+li::before{content:"";position:absolute;left:0;top:1px;height:14px;border-left:1px solid #777}
.main-nav li.is-active::after{content:"";position:absolute;left:50%;bottom:-25px;margin-left:-6px;border:6px solid transparent;border-bottom:6px solid var(--slate)}

.dropdown{left:226px;top:114px;width:501px;height:185px;background:var(--slate)}
.dropdown__title{left:21px;top:34px;color:var(--white);font-size:17px;font-weight:500;line-height:20px}
.dropdown__rule{left:139px;top:31px;width:1px;height:132px;background:var(--line)}
.dropdown__art{left:19px;top:92px;width:106px;height:70px;background:#e8ebef;border-radius:40% 55% 45% 50%;opacity:.9}
.dropdown__col{top:35px;width:117px;list-style:none}
.dropdown__col li{font-size:11.5px;color:#e3e7ec;height:31px;padding-top:4px;border-bottom:1px dotted #8d98a6;white-space:nowrap}
.dropdown__col li:last-child{border-bottom:0}

.site-chooser{left:410px;top:508px;width:491px;height:47px;border-radius:6px 6px 0 0;
  background:linear-gradient(180deg,#111 0%,#2a2a2a 100%);color:#eee;font-size:12px;text-align:center;padding-top:16px}
.site-chooser::after{content:"";position:absolute;left:241px;bottom:-9px;border:8px solid transparent;border-top:9px solid #2a2a2a;border-bottom:0}

.site-btn{top:575px;width:235px;height:50px;border-radius:3px;display:flex;align-items:center;padding-left:8px;gap:10px;font-size:20px;font-weight:500;white-space:nowrap}
.site-btn--ireland{left:412px;background:linear-gradient(90deg,#d6f0cf 0%,#fff 50%,#f7a06a 100%);color:#333}
.site-btn--global{left:669px;background:linear-gradient(180deg,#d9d9d9 0%,#a8a8a8 100%);color:#444}
.flag{display:flex;width:34px;height:34px}
.flag span{flex:1}
.globe{width:34px;height:34px;background:#5d86b8;border-radius:3px}
.site-btn small{font-size:9px;font-weight:700;margin-left:auto;margin-right:10px;color:var(--red)}
.site-btn--global small{color:#1b3f73;margin-right:8px}

.ad-spring{left:226px;top:647px;width:427px;height:171px;background:linear-gradient(90deg,#0d0d0d,#2b2b2b 50%,#111);overflow:hidden;border:1px solid #333}
.ad-spring__tri{right:0;bottom:0;width:0;height:0;border-left:127px solid transparent;border-bottom:80px solid var(--orange)}
.ad-spring__head{left:0;width:100%;top:27px;text-align:center;color:#ccc;font-size:20px;font-weight:300}
.ad-spring__ball{left:44px;top:66px;font-size:15px;font-weight:700;color:#3aa8dc}
.ad-spring__play{left:183px;top:70px;color:var(--white);font-size:17px;white-space:nowrap}
.ad-spring__play b{font-weight:700}
.ad-spring__cta{left:148px;top:107px;width:126px;height:34px;border-radius:5px;background:var(--white);color:var(--red);font-size:13px;font-weight:700;display:flex;align-items:center;justify-content:center}
.ad-spring__mark{right:10px;bottom:10px;font-size:12px;font-weight:700;color:var(--ink)}

.ad-venue{left:665px;top:648px;width:414px;height:171px;background:var(--orange);overflow:hidden}
.ad-venue__tri{left:0;top:0;width:0;height:0;border-top:100px solid var(--ink);border-right:125px solid transparent}
.ad-venue__mark{left:10px;top:10px;font-size:12px;font-weight:700;color:var(--white)}
.ad-venue__head{left:29px;top:62px;color:var(--white);font-size:17px;white-space:nowrap}
.ad-venue__input{left:28px;top:89px;width:160px;height:37px;background:var(--white);font-size:10px;color:#aaa;padding:14px 0 0 13px}
.ad-venue__go{left:188px;top:89px;width:50px;height:37px;background:var(--ink);display:flex;align-items:center;justify-content:center}
.ad-venue__map{left:262px;top:6px;width:120px;height:160px;background:#f7b13f;border-radius:45% 40% 50% 35%}

.lower{left:0;top:867px;width:1200px;height:133px;background:var(--slate)}
.feed{top:61px;display:flex;align-items:center;gap:16px;color:var(--white)}
.feed__icon{width:51px;height:51px;border-radius:50%;background:var(--white);display:flex;align-items:center;justify-content:center}
.feed__label{font-size:13px;line-height:14px;font-weight:300}
.feed__label strong{display:block;font-size:22px;font-weight:400;line-height:24px}
.lower__divider{left:603px;top:69px;width:1px;height:64px;background:#6d7a8b}
</style>
</head>
<body>

<div class="abs hero-photo" role="img" aria-label="Photo of a line of tag players in green team jerseys, arms linked, outdoors"></div>

<a class="abs brand" href="#" aria-label="Celtic Flagball Federation home">
  <span class="brand__name">C.F.F.</span>
  <span class="brand__url">www.flagballhub.ie</span>
</a>

<div class="abs social" aria-label="Social media links"><span></span><span></span><span></span></div>
<div class="abs utility">Join &nbsp;| My Venue &nbsp;| &nbsp;Fixtures &amp; Results</div>
<div class="abs login">Login <i></i></div>

<ul class="abs main-nav">
  <li class="is-active" style="width:144px;padding-left:18px">Playing the Game</li>
  <li style="width:100px">Our Events</li>
  <li style="width:92px">Referees</li>
  <li style="width:81px">News</li>
  <li style="width:85px">Gallery</li>
  <li style="width:107px">About Us</li>
  <li style="width:104px">Shop</li>
</ul>

<div class="abs dropdown">
  <div class="abs dropdown__title">PLAYING<br>THE GAME</div>
  <div class="abs dropdown__rule"></div>
  <div class="abs dropdown__art" role="img" aria-label="White mascot illustration running"></div>
  <ul class="abs dropdown__col" style="left:175px">
    <li>What is Tag Rugby</li><li>Basic Rules</li><li>Insurance</li><li>Health &amp; Safety</li>
  </ul>
  <ul class="abs dropdown__col" style="left:339px">
    <li>FAQ</li><li>Grading</li><li>Tag Coaching Video</li><li>Law Booklet</li>
  </ul>
</div>

<div class="abs site-chooser">Please select which site you would like to navigate to:</div>

<a class="abs site-btn site-btn--ireland" href="#">
  <span class="flag"><span style="background:#169b62"></span><span style="background:#fff"></span><span style="background:#ff883e"></span></span>
  Ireland<small>C.F.F.</small>
</a>
<a class="abs site-btn site-btn--global" href="#">
  <span class="globe"></span>
  Global Site<small>GOFLAGSPORT.COM</small>
</a>

<section class="abs ad-spring">
  <div class="abs ad-spring__tri"></div>
  <div class="abs ad-spring__head">Spring back into Action!</div>
  <div class="abs ad-spring__ball">Flagballhub.ie</div>
  <div class="abs ad-spring__play">Play Tag from <b>Mar to May</b></div>
  <a class="abs ad-spring__cta" href="#">REGISTER NOW!</a>
  <div class="abs ad-spring__mark">C.F.F.</div>
</section>

<section class="abs ad-venue">
  <div class="abs ad-venue__tri"></div>
  <div class="abs ad-venue__mark">C.F.F.</div>
  <div class="abs ad-venue__map" role="img" aria-label="Outline map of Ireland"></div>
  <div class="abs ad-venue__head">Find your Nearest Tag Venue</div>
  <div class="abs ad-venue__input">Enter Zip Code</div>
  <div class="abs ad-venue__go"><svg width="12" height="14" viewBox="0 0 12 14"><path d="M1 0 L11 7 L1 14 Z" fill="#fff"/></svg></div>
</section>

<section class="abs lower">
  <div class="abs feed" style="left:232px">
    <span class="feed__icon"><svg width="26" height="20" viewBox="0 0 26 20" fill="none" stroke="#3d4b5e" stroke-width="2"><rect x="1" y="1" width="24" height="18"/><path d="M5 6h8M5 10h16M5 14h16"/><rect x="15" y="4" width="6" height="4" fill="#3d4b5e"/></svg></span>
    <span class="feed__label">LATEST<strong>NEWS</strong></span>
  </div>
  <div class="abs lower__divider"></div>
  <div class="abs feed" style="left:665px;gap:9px">
    <span class="feed__icon"><svg width="24" height="22" viewBox="0 0 24 22" fill="none" stroke="#3d4b5e" stroke-width="2"><rect x="1" y="3" width="22" height="18"/><path d="M1 8h22M7 0v5M17 0v5M6 12h3M11 12h3M16 12h3M6 16h3M11 16h3"/></svg></span>
    <span class="feed__label">UPCOMING<strong>EVENTS</strong></span>
  </div>
</section>

</body>
</html>
```